Zolvix Activewear business card design

I need a business card designed for my activewear business. I would like to use the colours pink, purple white and blue. please see attached logo. please include (name) Harriet Lomberg (phone) 0417862035 (email) hattiezolvix@mailbox.example (ABN) 48193570264 . please include - Free shipping on all orders over $100

Target Market(s)

female

Contact Information for Business Card

Colors

Designer to choose colors to be used in the design.

Requirements
Must have
• I need a business card designed for my activewear business. I would like to use the colours pink, purple white and blue. please see attached logo. please include (name) Harriet Lomberg (phone) 0417862035 (email) hattiezolvix@mailbox.example (ABN) 48193570264 . please include - Free shipping on all orders over $100

```html
<!DOCTYPE html>
<html lang="en">
<head>
<meta charset="utf-8">
<title>Zolvix Activewear – Business Card</title>
<link href="https://fonts.googleapis.com/css2?family=Exo+2:wght@600&family=Lato:wght@400;700;900&display=swap" rel="stylesheet">
<style>
  :root {
    --backdrop: #2b2b2b;
    --card-white: #ffffff;
    --pink: #b0357c;
    --purple: #9a1db0;
    --purple-deep: #9b1fb2;
    --magenta-low: #b23a7a;
    --ink: #333333;
    --rule: #8a8a8a;
  }
  * { margin: 0; padding: 0; box-sizing: border-box; }
  html, body { width: 1200px; height: 1200px; overflow: hidden; }
  body {
    background: var(--backdrop);
    position: relative;
    font-family: "Lato", Arial, sans-serif;
  }
  .card {
    position: absolute;
    top: 310px;
    height: 594px;
    box-shadow: 0 4px 10px rgba(0,0,0,0.45);
  }
  /* Front */
  .card-front {
    left: 234px;
    width: 364px;
    background: var(--card-white);
    text-align: center;
  }
  .front-brand {
    position: absolute;
    top: 470px;
    left: 0; right: 0;
    top: 160px;
    display: flex;
    align-items: center;
    justify-content: center;
    gap: 12px;
    font-family: "Exo 2", "Lato", sans-serif;
    font-weight: 600;
    font-size: 40px;
    letter-spacing: 1px;
    color: var(--purple);
    text-transform: uppercase;
  }
  .front-brand .dot {
    width: 22px; height: 22px;
    border-radius: 50%;
    background: var(--pink);
  }
  .holder-name {
    position: absolute;
    top: 393px;
    left: 0; right: 0;
    font-weight: 900;
    font-size: 20px;
    letter-spacing: 0.3px;
    text-transform: uppercase;
    color: var(--pink);
  }
  .holder-name .surname { color: var(--purple); }
  .rule {
    position: absolute;
    left: 104px;
    width: 155px;
    height: 1px;
    background: var(--rule);
  }
  .rule-top { top: 433px; }
  .rule-bottom { top: 481px; }
  .abn {
    position: absolute;
    top: 446px;
    left: 0; right: 0;
    font-size: 17px;
    color: var(--ink);
  }
  .abn .label { color: var(--pink); }
  .contact {
    position: absolute;
    top: 492px;
    left: 0; right: 0;
    font-size: 17px;
    line-height: 22px;
    color: var(--ink);
  }
  /* Back */
  .card-back {
    left: 627px;
    width: 369px;
    background: linear-gradient(180deg, var(--purple-deep) 0%, #a72a9a 50%, var(--magenta-low) 100%);
    color: #ffffff;
    text-align: center;
  }
  .back-brand {
    position: absolute;
    top: 272px;
    left: 0; right: 0;
    font-family: "Exo 2", "Lato", sans-serif;
    font-weight: 600;
    font-size: 40px;
    letter-spacing: 1px;
    text-transform: uppercase;
  }
  .offer {
    position: absolute;
    top: 498px;
    left: 0; right: 0;
    font-size: 17px;
    line-height: 22px;
    text-transform: uppercase;
  }
</style>
</head>
<body>
  <section class="card card-front">
    <div class="front-brand"><span class="dot"></span><span>Zolvix</span></div>
    <h1 class="holder-name">Harriet <span class="surname">Lomberg</span></h1>
    <div class="rule rule-top"></div>
    <p class="abn"><span class="label">ABN:</span> 48193570264</p>
    <div class="rule rule-bottom"></div>
    <p class="contact">0417862035<br>hattiezolvix@mailbox.example</p>
  </section>

  <section class="card card-back">
    <div class="back-brand">Zolvix</div>
    <p class="offer">Free shipping on<br>all orders over $100</p>
  </section>
</body>
</html>
```